TKR Website Overhaul. Complete new website look and function.

Need our website overhauled to be updated so it aligns better with our current cliental. We have competitors to compare to. The purpose of the site has changed and is no longer sales based. This site needs to qualify us and allow consultants and engineers to just discover our background and differentiators. I have attached a company profile from a recent project to provide a better idea. This profile is directed towards the specific project however so that would need to be edited out. Competitor websites that we would want to be comparable to would include: https://www.velmoran.com/ , https://brimleyconstruction.ca/ , https://www.tuskconstruction.ca/ , https://steadfastdiggers.com/ , https://www.hallowayconstruction.ca/. These are all competitors so nothing can be directly copied. I have attached our logo's however I don't think they need to be directly used on the site or maybe they need to be changed to not include color etc. We need to have a more professional look and these colorful logos are hard to pull that off with other than maybe the all gold TKR prime contracting logo with a rich dark green background or something. Green has been our main color over the years and the leaf follows us as the core item in logos. Go with a gold leaf look or something. Our main focus is General Contracting (Prime Contracting) and civil construction. We are a home builder however we would do a second website for that so we don't want to include it. I don't mind a ton of generic civil and general contractor information etc on the site. I don't really need a portfolio of pictures showing on the site but job history etc is very common in the industry and that information can be found in the company profile attached. First Nation work is a big part of our portfolio but we have worked in mining, industrial, oil and gas as well. Municipal sewer and water is our main focus for civil construction though and is a big part of our First Nation work as well.

Industry/Entity Type

General Contractor and Civil Construction

Coding

Coded - Design and coding required

Number of Pages Required

5+ page

Font styles to use
Other font styles liked:
• A mix of Times New Roman, script and serif to create a very professional with a touch of elegance to match our leafed prime contractor logo.

Colors
00AB8E
00BBA5
67D7C9
C6EFE9
E9F9F6

Requirements
Must have
• A rich high end professional look. This company completes government work and is often looked at by executives. A menu that includes About, Our Work, Methodology, Join Our Team and Contact
Nice to have
• Some generic general pictures of municipal underground water work and general contractor building work. I am looking for a rich green darker greens where it matters but with more real world feel overall. So images and movement is good. Civil underground water and sewer, storm water, retention ponds, and process plant and electrical (such as water treatment plants), background imagery is good to have. I like to have things faded out in the background more than in your face.
Should not have
• brighter colors.

```html
<!DOCTYPE html>
<html lang="en">
<head>
<meta charset="utf-8">
<title>TKR Prime Contracting</title>
<link href="https://fonts.googleapis.com/css2?family=Tinos:wght@400;700&family=Lato:wght@400;700&family=Poppins:wght@400;500&display=swap" rel="stylesheet">
<style>
:root{
  --green:#00ab8e;
  --green-2:#00bba5;
  --teal-deep:#0b8f7b;
  --mint:#c6eff9;
  --gold:#c9962e;
  --gold-dark:#b98522;
  --ink:#1e1e1e;
  --text:#4a4a4a;
  --footer:#1d1d1d;
  --white:#ffffff;
}
*{box-sizing:border-box;margin:0;padding:0}
html,body{width:1200px;height:3449px;overflow:hidden;background:var(--white)}
body{position:relative;font-family:"Lato",sans-serif;color:var(--text)}
.abs{position:absolute}

/* header */
.site-header{position:absolute;left:0;top:0;width:1200px;height:73px;background:var(--white);z-index:5}
.brand-badge{position:absolute;left:110px;top:-20px;width:174px;height:174px;border-radius:50%;background:var(--white);box-shadow:0 2px 8px rgba(0,0,0,.18);display:flex;align-items:center;justify-content:center;z-index:6}
.brand-badge span{font-family:"Tinos",serif;font-size:44px;color:var(--gold);letter-spacing:1px;margin-top:24px}
.main-nav{position:absolute;left:363px;top:23px;display:flex;gap:8px;font-family:"Tinos",serif;font-size:17px;color:var(--ink)}
.main-nav a{display:block;padding:6px 14px;border-radius:18px;color:var(--ink);text-decoration:none;line-height:20px}
.main-nav a.active{background:var(--green);color:var(--white);font-weight:700;padding:6px 17px}
.main-nav a+a{margin-left:12px}
.btn{display:inline-block;border-radius:22px;font-family:"Tinos",serif;font-weight:700;text-transform:uppercase;color:var(--white);text-align:center;letter-spacing:.5px}
.btn-gold{background:var(--gold)}
.btn-green{background:var(--green)}
.header-contact{position:absolute;left:973px;top:15px;width:114px;height:40px;line-height:40px;font-size:15px}

/* hero */
.hero{position:absolute;left:0;top:73px;width:1200px;height:583px;background:linear-gradient(160deg,#5c5a52 0%,#3b3a35 45%,#23262a 100%)}
.hero::after{content:"";position:absolute;inset:0;background:rgba(20,20,20,.35)}
.hero-title{position:absolute;left:0;top:178px;width:1200px;text-align:center;font-family:"Tinos",serif;font-weight:700;font-size:66px;line-height:78px;color:var(--white);z-index:2}
.hero-title .gold{color:var(--gold)}
.hero-cta{position:absolute;left:513px;top:427px;width:174px;height:40px;line-height:40px;font-size:15px;z-index:2}

/* about */
.section-title{font-family:"Tinos",serif;font-size:43px;color:var(--ink);font-weight:400}
.section-title b{font-weight:700;color:var(--green)}
.about-title{left:110px;top:738px}
.title-rule{position:absolute;height:2px;background:var(--gold)}
.title-rule::after{content:"";position:absolute;right:-4px;top:-3px;width:8px;height:8px;border-radius:50%;background:var(--gold)}
.about-copy{left:110px;top:808px;width:443px;font-size:12.6px;line-height:31px;text-align:justify;letter-spacing:-.1px}
.about-copy p+p{margin-top:7px}
.about-more{left:112px;top:1141px;width:126px;height:42px;line-height:42px;font-size:15px}
.photo{position:absolute}
.about-photo-main{left:738px;top:743px;width:350px;height:434px;background:linear-gradient(180deg,#c7d3dc 0%,#9aa1a3 35%,#6e6a63 70%,#514b44 100%)}
.about-photo-inset{left:644px;top:928px;width:240px;height:249px;background:linear-gradient(160deg,#8a6a4a,#5b4330 60%,#3e3b3a);outline:8px solid var(--white)}

/* sectors */
.sectors{position:absolute;left:0;top:1265px;width:1200px;height:502px;background:linear-gradient(180deg,#15a58e 0%,#109c86 55%,#0d8a77 100%)}
.sectors-title{position:absolute;left:0;top:62px;width:1200px;text-align:center;font-family:"Tinos",serif;font-size:43px;font-weight:400;color:var(--white)}
.sectors-title b{font-weight:700}
.sector-highlight{position:absolute;left:690px;top:0;width:220px;height:502px;background:linear-gradient(180deg,#7a5320 0%,#b07a2c 45%,#8a5e24 100%)}
.sector{position:absolute;top:210px;width:200px;text-align:center;color:var(--white);font-family:"Tinos",serif;font-weight:700;font-size:21px;line-height:30px}
.sector svg{display:block;margin:0 auto 34px}
.sector-more{display:block;margin:14px auto 0;width:126px;height:38px;line-height:38px;font-size:14px}

/* capabilities */
.cap-photo{left:111px;top:1853px;width:446px;height:350px;background:linear-gradient(135deg,#7a4e22 0%,#3a2b22 40%,#1d3346 75%,#2f6d8e 100%)}
.cap-title{left:644px;top:1843px}
.cap-list{position:absolute;left:644px;top:1922px;list-style:none;font-family:"Tinos",serif;font-size:16.5px;color:#555}
.cap-list li{display:flex;align-items:center;height:40px}
.cap-list svg{margin-right:10px}

/* careers */
.careers{position:absolute;left:111px;top:2302px;width:977px;height:334px;background:linear-gradient(120deg,#17b397 0%,#0ea88f 60%,#0b9a84 100%);text-align:center;color:var(--white)}
.careers h2{font-family:"Tinos",serif;font-size:43px;line-height:52px;font-weight:700;margin-top:44px}
.careers h3{font-family:"Tinos",serif;font-size:41px;line-height:50px;font-weight:400}
.careers p{width:590px;margin:20px auto 0;font-size:11.5px;line-height:23px}
.careers .btn{margin-top:20px;width:166px;height:41px;line-height:41px;font-size:15px}

/* methodology */
.method-title{left:113px;top:2706px}
.method-step{position:absolute;top:2808px;width:160px;text-align:center;font-size:14.5px;line-height:23px;color:#333}
.method-step .dot{width:78px;height:78px;border-radius:50%;margin:0 auto 30px;display:flex;align-items:center;justify-content:center}
.dot.gold{background:var(--gold)}
.dot.green{background:var(--green)}
.method-step.feature .dot{width:82px;height:82px;margin-bottom:44px;box-shadow:0 0 0 9px #fff,0 0 0 11px var(--green)}
.arrow{position:absolute;top:2848px}

/* footer */
.site-footer{position:absolute;left:0;top:3080px;width:1200px;height:369px;background:var(--footer);color:var(--white)}
.footer-head{position:absolute;top:76px;font-family:"Lato",sans-serif;font-size:21px;color:var(--gold)}
.quick-links{position:absolute;left:113px;top:121px;list-style:none;font-size:14.5px;line-height:30px}
.footer-brand{position:absolute;left:521px;top:76px;width:160px;height:160px;border-radius:50%;border:2px solid var(--gold);display:flex;align-items:center;justify-content:center;font-family:"Tinos",serif;font-size:52px;color:var(--gold)}
.socials{position:absolute;left:533px;top:262px;display:flex;gap:8px}
.socials span{width:28px;height:28px;border-radius:50%;background:var(--white);border:2px solid var(--gold)}
.contact-list{position:absolute;left:862px;top:112px;list-style:none;font-size:14px;line-height:30px}
.contact-list li{display:flex;align-items:flex-start;margin-bottom:21px}
.contact-list svg{flex:none;margin:5px 14px 0 0}
.footer-rule{position:absolute;left:110px;top:325px;width:977px;height:1px;background:#777}
.copyright{position:absolute;left:0;top:336px;width:1200px;text-align:center;font-family:"Poppins",sans-serif;font-size:13px;letter-spacing:1.2px}
</style>
</head>
<body>

<header class="site-header">
  <div class="brand-badge"><span>TKR</span></div>
  <nav class="main-nav">
    <a class="active">Home</a><a>About</a><a>Our Work</a><a>Methodology</a><a>Join Our Team</a>
  </nav>
  <span class="btn btn-gold header-contact">Contact</span>
</header>

<section class="hero" role="img" aria-label="Underground pipe installation site with large wrapped pipes and crew in hard hats">
  <h1 class="hero-title"><span class="gold">Prime Contracting &amp; Civil</span><br>Construction for Critical<br>Infrastructure</h1>
  <span class="btn btn-green hero-cta">View Our Work</span>
</section>

<h2 class="section-title abs about-title">About <b>Us</b></h2>
<div class="title-rule" style="left:112px;top:794px;width:50px"></div>
<div class="abs about-copy">
  <p>Tallkeel Ridge Enterprises Ltd. is a Ridgefield, Alberta–based construction management and civil infrastructure company with over 15 years of experience delivering complex public infrastructure projects across Alberta. The company specializes in practical, solution-driven construction services with a strong focus on safety, collaboration, accountability, and community-based delivery.</p>
  <p>For the Cedarbrook First Nation – Pine Hollow Water Treatment Plant (WTP), Contract 3 – General Construction, Tallkeel Ridge Enterprises Ltd. brings direct experience working within First Nation communities and delivering water-related infrastructure under consulting engineer–led contracts.</p>
</div>
<span class="btn btn-gold abs about-more">Read More</span>
<div class="photo about-photo-main" role="img" aria-label="Building construction site with crane, trucks and a forklift operator"></div>
<div class="photo about-photo-inset" role="img" aria-label="Worker in safety vest inspecting a buried pipe with a tablet"></div>

<section class="sectors" role="img" aria-label="Faded construction cranes and building frames behind the sector list">
  <div class="sector-highlight" role="img" aria-label="Oil pumpjack at sunset"></div>
  <h2 class="sectors-title">Sectors <b>We Serve</b></h2>
  <div class="title-rule" style="left:573px;top:123px;width:50px"></div>

  <div class="sector" style="left:80px">
    <svg width="72" height="70" viewBox="0 0 72 70" fill="#fff"><rect x="14" y="14" width="12" height="24"/><rect x="30" y="4" width="14" height="34"/><rect x="48" y="16" width="10" height="22"/><rect x="4" y="38" width="64" height="6"/><path d="M14 48h44a22 22 0 0 1-44 0z"/></svg>
    First Nation<br>Infrastructure
  </div>
  <div class="sector" style="left:298px;top:205px">
    <svg width="62" height="62" viewBox="0 0 62 62" fill="#fff"><path d="M10 28a21 21 0 0 1 42 0z"/><rect x="8" y="30" width="46" height="4"/><rect x="12" y="36" width="7" height="14"/><rect x="27" y="36" width="7" height="14"/><rect x="42" y="36" width="7" height="14"/><rect x="4" y="52" width="54" height="6"/></svg>
    Municipal<br>Governments
  </div>
  <div class="sector" style="left:479px">
    <svg width="74" height="56" viewBox="0 0 74 56" fill="#fff"><path d="M4 10h40l6 20H8z"/><path d="M50 18h12l8 12v10H50z"/><rect x="6" y="30" width="64" height="8"/><circle cx="18" cy="44" r="8"/><circle cx="58" cy="44" r="8"/></svg>
    Mining
  </div>
  <div class="sector" style="left:700px;top:200px">
    <svg width="50" height="62" viewBox="0 0 50 62" fill="#fff"><rect x="4" y="2" width="42" height="6"/><rect x="4" y="54" width="42" height="6"/><rect x="8" y="10" width="34" height="42"/><path d="M25 20c5 7 8 11 8 15a8 8 0 0 1-16 0c0-4 3-8 8-15z" fill="#8a5e24"/></svg>
    Oil &amp; Gas
    <span class="btn btn-green sector-more">Read More</span>
  </div>
  <div class="sector" style="left:912px">
    <svg width="56" height="56" viewBox="0 0 56 56" fill="#fff"><rect x="6" y="14" width="8" height="40"/><path d="M14 54V30l12 8v-8l12 8v-8l12 8v16z"/><circle cx="20" cy="8" r="5"/><circle cx="30" cy="10" r="6"/><circle cx="42" cy="8" r="5"/></svg>
    Industrial<br>Facilities
  </div>
</section>

<div class="photo cap-photo" role="img" aria-label="Bulldozers working in a lit underground tunnel"></div>
<h2 class="section-title abs cap-title">Core <b>Capabilities</b></h2>
<ul class="cap-list">
  <li><svg width="20" height="20" viewBox="0 0 20 20"><path d="M3 17C3 8 9 3 18 2c0 9-5 15-14 15z" fill="none" stroke="#00ab8e" stroke-width="2"/><path d="M3 17L13 7" stroke="#00ab8e" stroke-width="2"/></svg>Construction Management &amp; Project Controls</li>
  <li><svg width="20" height="20" viewBox="0 0 20 20"><path d="M3 17C3 8 9 3 18 2c0 9-5 15-14 15z" fill="none" stroke="#00ab8e" stroke-width="2"/><path d="M3 17L13 7" stroke="#00ab8e" stroke-width="2"/></svg>Civil Infrastructure &amp; Earthworks</li>
  <li><svg width="20" height="20" viewBox="0 0 20 20"><path d="M3 17C3 8 9 3 18 2c0 9-5 15-14 15z" fill="none" stroke="#00ab8e" stroke-width="2"/><path d="M3 17L13 7" stroke="#00ab8e" stroke-width="2"/></svg>Water &amp; Wastewater Systems</li>
  <li><svg width="20" height="20" viewBox="0 0 20 20"><path d="M3 17C3 8 9 3 18 2c0 9-5 15-14 15z" fill="none" stroke="#00ab8e" stroke-width="2"/><path d="M3 17L13 7" stroke="#00ab8e" stroke-width="2"/></svg>Underground Utilities &amp; Site Services</li>
  <li><svg width="20" height="20" viewBox="0 0 20 20"><path d="M3 17C3 8 9 3 18 2c0 9-5 15-14 15z" fill="none" stroke="#00ab8e" stroke-width="2"/><path d="M3 17L13 7" stroke="#00ab8e" stroke-width="2"/></svg>Concrete Works, Foundations &amp; Building Structures</li>
  <li><svg width="20" height="20" viewBox="0 0 20 20"><path d="M3 17C3 8 9 3 18 2c0 9-5 15-14 15z" fill="none" stroke="#00ab8e" stroke-width="2"/><path d="M3 17L13 7" stroke="#00ab8e" stroke-width="2"/></svg>Mechanical, Electrical &amp; Process Coordination</li>
  <li><svg width="20" height="20" viewBox="0 0 20 20"><path d="M3 17C3 8 9 3 18 2c0 9-5 15-14 15z" fill="none" stroke="#00ab8e" stroke-width="2"/><path d="M3 17L13 7" stroke="#00ab8e" stroke-width="2"/></svg>Commissioning &amp; Turnover Support</li>
</ul>

<section class="careers" role="img" aria-label="Faded excavator silhouette behind the careers message">
  <h2>Careers Supporting</h2>
  <h3>Community Infrastructure</h3>
  <p>Tallkeel Ridge Enterprises LTD offers long-term career opportunities for professionals who value quality workmanship, safety, and accountability. Our teams deliver essential civil infrastructure and prime contracting projects that serve communities, municipalities, and Indigenous partners.</p>
  <span class="btn btn-gold">Join Our Team</span>
</section>

<h2 class="section-title abs method-title">Our <b>Methodology</b></h2>

<div class="method-step" style="left:95px">
  <div class="dot gold"><svg width="36" height="36" viewBox="0 0 36 36" fill="none" stroke="#fff" stroke-width="2.5"><rect x="4" y="8" width="24" height="24"/><path d="M10 14h12M10 20h12M10 26h7M24 4l8 8-10 10h-8v-8z"/></svg></div>
  Pre-Construction<br>Planning
</div>
<div class="method-step" style="left:308px">
  <div class="dot green"><svg width="38" height="30" viewBox="0 0 38 30" fill="#fff"><circle cx="10" cy="7" r="5"/><circle cx="28" cy="7" r="5"/><circle cx="19" cy="10" r="5"/><path d="M2 24c0-6 4-9 8-9s6 2 9 2 5-2 9-2 8 3 8 9z"/></svg></div>
  Stakeholder &amp;<br>Community<br>Coordination
</div>
<div class="method-step feature" style="left:521px;top:2806px">
  <div class="dot gold"><svg width="34" height="38" viewBox="0 0 34 38"><path d="M17 2l14 6v10c0 9-6 15-14 18C9 33 3 27 3 18V8z" fill="#fff"/><path d="M11 19l5 5 8-9" stroke="#c9962e" stroke-width="3" fill="none"/></svg></div>
  Safety &amp;<br>Environmental<br>Compliance
</div>
<div class="method-step" style="left:735px">
  <div class="dot green"><svg width="40" height="40" viewBox="0 0 40 40" fill="none" stroke="#fff" stroke-width="4"><circle cx="20" cy="11" r="5"/><circle cx="10" cy="28" r="5"/><circle cx="30" cy="28" r="5"/></svg></div>
  Construction<br>Execution
</div>
<div class="method-step" style="left:948px">
  <div class="dot gold"><svg width="34" height="38" viewBox="0 0 34 38" fill="none" stroke="#fff" stroke-width="2.5"><path d="M6 2h16l8 8v26H6z"/><path d="M12 30v-6M18 30v-10M24 30v-4"/><circle cx="14" cy="12" r="5"/></svg></div>
  Reporting &amp;<br>Close-Out
</div>

<svg class="arrow" style="left:225px" width="100" height="24" viewBox="0 0 100 24" fill="none" stroke="#333" stroke-width="1.3" stroke-dasharray="3 3"><path d="M2 8c20 16 60 16 92 2"/><path d="M86 6l8 4-6 6" stroke-dasharray="none"/></svg>
<svg class="arrow" style="left:438px" width="100" height="24" viewBox="0 0 100 24" fill="none" stroke="#333" stroke-width="1.3" stroke-dasharray="3 3"><path d="M2 16C30 0 70 0 94 14"/><path d="M86 16l8-2-3-7" stroke-dasharray="none"/></svg>
<svg class="arrow" style="left:652px" width="100" height="24" viewBox="0 0 100 24" fill="none" stroke="#333" stroke-width="1.3" stroke-dasharray="3 3"><path d="M2 8c20 16 60 16 92 2"/><path d="M86 6l8 4-6 6" stroke-dasharray="none"/></svg>
<svg class="arrow" style="left:865px" width="100" height="24" viewBox="0 0 100 24" fill="none" stroke="#333" stroke-width="1.3" stroke-dasharray="3 3"><path d="M2 16C30 0 70 0 94 14"/><path d="M86 16l8-2-3-7" stroke-dasharray="none"/></svg>

<footer class="site-footer">
  <div class="footer-head" style="left:110px">Quick Links</div>
  <ul class="quick-links">
    <li>Home</li><li>About</li><li>Our Work</li><li>Methodology</li><li>Join Our Team</li><li>Contact</li>
  </ul>
  <div class="footer-brand">TKR</div>
  <div class="socials" aria-label="Social profiles"><span></span><span></span><span></span><span></span></div>
  <div class="footer-head" style="left:862px">Contact info</div>
  <ul class="contact-list">
    <li><svg width="24" height="24" viewBox="0 0 24 24"><circle cx="12" cy="12" r="12" fill="#fff"/><path d="M12 5a5 5 0 0 0-5 5c0 4 5 9 5 9s5-5 5-9a5 5 0 0 0-5-5z" fill="#1d1d1d"/><circle cx="12" cy="10" r="2" fill="#fff"/></svg><span>Tallkeel Ridge Enterprises Ltd.<br>Box 218 Ridgefield Alberta T0X1A0</span></li>
    <li><svg width="24" height="24" viewBox="0 0 24 24"><circle cx="12" cy="12" r="12" fill="#fff"/><path d="M8 6l3 3-1.5 2a9 9 0 0 0 3.5 3.5L15 13l3 3-2 2c-5 0-10-5-10-10z" fill="#1d1d1d"/></svg><span>(555) 010 4827</span></li>
    <li><svg width="24" height="24" viewBox="0 0 24 24"><circle cx="12" cy="12" r="12" fill="#fff"/><rect x="6" y="8" width="12" height="9" fill="#1d1d1d"/><path d="M6 8l6 5 6-5" stroke="#fff" fill="none"/></svg><span>info@tkrprimecontracting.com</span></li>
  </ul>
  <div class="footer-rule"></div>
  <div class="copyright">© 2025 TKR PRIME CONTRACTING.All Rights Reserved</div>
</footer>

</body>
</html>
```